" Nós somos integradores de TI, nós fornecemos soluções de segurança e infraestrutura de TI para o mercado corporativo. Somos parceiros de empresas como Tarvok, Brix, Nuvexa, Quintorial entre outras. Nossos clientes são empresas e governos, mais especificamente os profissionais de TI destas empresas. "

```html
<!DOCTYPE html>
<html lang="pt-BR">
<head>
<meta charset="utf-8">
<title>Corvanta – Cartão de Visita</title>
<link href="https://fonts.googleapis.com/css2?family=Open+Sans:wght@400;600;700&display=swap" rel="stylesheet">
<style>
  :root {
    --bg: #e9e7e4;
    --card: #ffffff;
    --red: #e3262b;
    --grey-band: #5a5a5c;
    --ink: #1a1a1a;
    --muted: #55575a;
  }
  * { box-sizing: border-box; margin: 0; padding: 0; }
  html, body { width: 1200px; height: 1200px; overflow: hidden; }
  body {
    background: var(--bg);
    font-family: "Open Sans", Arial, sans-serif;
    color: var(--ink);
    position: relative;
  }
  .card {
    position: absolute;
    left: 162px;
    width: 876px;
    height: 494px;
    background: var(--card);
    box-shadow: 0 6px 18px rgba(0,0,0,.18);
    overflow: hidden;
  }
  .card--front { top: 72px; }
  .card--back { top: 636px; }
  .band-top {
    position: absolute; top: 0; left: 0; right: 0; height: 13px;
    background: var(--red);
  }
  .band-bottom {
    position: absolute; bottom: 0; left: 0; right: 0; height: 13px;
    display: flex;
  }
  .band-bottom .grey { width: 50%; background: var(--grey-band); }
  .band-bottom .red { width: 50%; background: var(--red); }

  .brand { position: absolute; display: flex; flex-direction: column; align-items: center; }
  .brand-name {
    font-family: "Open Sans", Arial, sans-serif;
    font-weight: 600;
    color: var(--ink);
    line-height: 1;
    text-transform: uppercase;
    white-space: nowrap;
  }
  .brand-tagline {
    font-family: "Open Sans", Arial, sans-serif;
    font-weight: 400;
    color: var(--muted);
    text-transform: uppercase;
    white-space: nowrap;
  }

  .card--front .brand { left: 0; right: 0; top: 208px; }
  .card--front .brand-name { font-size: 70px; letter-spacing: 12px; }
  .card--front .brand-tagline { font-size: 18px; letter-spacing: 4px; margin-top: 14px; }

  .card--back .brand { left: 56px; width: 340px; top: 222px; }
  .card--back .brand-name { font-size: 33px; letter-spacing: 5px; }
  .card--back .brand-tagline { font-size: 9.5px; letter-spacing: 2px; margin-top: 7px; }

  .contact { position: absolute; left: 458px; top: 100px; }
  .person-name { font-size: 34px; font-weight: 600; line-height: 1.1; }
  .person-role { font-size: 21px; font-weight: 600; margin-top: 2px; }
  .contact-list { list-style: none; margin-top: 22px; }
  .contact-list li {
    display: flex; align-items: center; gap: 16px;
    font-size: 17px; font-weight: 600; height: 44px;
  }
  .icon { width: 28px; height: 28px; flex: none; }
</style>
</head>
<body>

<section class="card card--front">
  <div class="band-top"></div>
  <div class="brand">
    <div class="brand-name">Corvanta</div>
    <div class="brand-tagline">Tecnologia para negócios</div>
  </div>
  <div class="band-bottom"><div class="grey"></div><div class="red"></div></div>
</section>

<section class="card card--back">
  <div class="band-top"></div>
  <div class="brand">
    <div class="brand-name">Corvanta</div>
    <div class="brand-tagline">Tecnologia para negócios</div>
  </div>

  <div class="contact">
    <div class="person-name">Nome Sobrenome</div>
    <div class="person-role">cargo</div>
    <ul class="contact-list">
      <li>
        <svg class="icon" viewBox="0 0 28 28" aria-hidden="true">
          <circle cx="14" cy="14" r="12.5" fill="none" stroke="#e3262b" stroke-width="2"/>
          <path d="M10 8.5c.8-.6 1.6-.3 2 .5l1 2c.3.7 0 1.2-.5 1.6l-.6.5c.6 1.4 1.7 2.6 3 3.3l.6-.6c.5-.5 1-.6 1.6-.3l2 1c.8.4 1 1.3.4 2-1 1.2-2.5 1.5-4 .8-3-1.4-5.3-3.8-6.4-6.9-.5-1.6-.1-3 .9-3.9z" fill="#e3262b"/>
        </svg>
        +55 11 9999-8888
      </li>
      <li>
        <svg class="icon" viewBox="0 0 28 28" aria-hidden="true">
          <circle cx="14" cy="14" r="13" fill="#e3262b"/>
          <rect x="9.5" y="6" width="9" height="16" rx="1.6" fill="#fff"/>
          <rect x="11" y="8" width="6" height="10.5" fill="#e3262b"/>
          <circle cx="14" cy="20.2" r="0.9" fill="#e3262b"/>
        </svg>
        +55 11 9 9999-8888
      </li>
      <li>
        <svg class="icon" viewBox="0 0 28 28" aria-hidden="true">
          <circle cx="14" cy="14" r="13" fill="#e3262b"/>
          <g fill="none" stroke="#fff" stroke-width="1.6">
            <circle cx="14" cy="14" r="8"/>
            <ellipse cx="14" cy="14" rx="3.5" ry="8"/>
            <path d="M6 14h16M7.5 10h13M7.5 18h13"/>
          </g>
        </svg>
        www.corvanta.com.br
      </li>
      <li>
        <svg class="icon" viewBox="0 0 28 28" aria-hidden="true">
          <path d="M14 2.5c-5 0-8.8 3.8-8.8 8.6 0 6.2 8.8 14.4 8.8 14.4s8.8-8.2 8.8-14.4c0-4.8-3.8-8.6-8.8-8.6z" fill="#e3262b"/>
          <circle cx="14" cy="11" r="3.4" fill="#fff"/>
        </svg>
        Endereço: Exemplo - Exemplo
      </li>
      <li>
        <svg class="icon" viewBox="0 0 28 28" aria-hidden="true">
          <rect x="3" y="7" width="22" height="15" rx="1.5" fill="#e3262b"/>
          <path d="M3.5 8l10.5 8 10.5-8" fill="none" stroke="#fff" stroke-width="1.6"/>
        </svg>
        contato@corvanta.com.br
      </li>
    </ul>
  </div>
  <div class="band-bottom"><div class="grey"></div><div class="red"></div></div>
</section>

</body>
</html>
```